Brixtondel - eCommerce Design and Shopify Theme customisation

eCommerce Website Design - firstly with mockups then once we have chosen the design the successful designer will need to choose, purchase and customise a Shopify theme to match the design. We have a logo already designed and now want to create our web presence based on carrying up to 50 products on our website.
Target Market(s)
UK Pet Owners
Industry/Entity Type
Pet Shop
Requirements
Must have
- Design must be achievable using a customised Shopify theme - the successful designer will be responsible for the delivery of a working theme on our shopify website.
Should not have
- should not look cheap or have designs that aren't compatible or achievable with Shopify

```html
<!DOCTYPE html>
<html lang="en">
<head>
<meta charset="utf-8">
<title>Brixtondel — Pet Supplies</title>
<link href="https://fonts.googleapis.com/css2?family=Montserrat:wght@300;400;500;600;700&display=swap" rel="stylesheet">
<style>
:root{
  --yellow:#fdc117;
  --ink:#2b2b2b;
  --muted:#777;
  --grey-btn:#9b9b9b;
  --footer:#efefef;
  --price:#e8603c;
  --line:#e6e6e6;
  --white:#fff;
}
*{margin:0;padding:0;box-sizing:border-box}
html,body{width:1200px;height:1200px;overflow:hidden;background:var(--white)}
body{font-family:'Montserrat',sans-serif;color:var(--ink);position:relative}
.page{position:absolute;left:373px;top:0;width:569px;height:1500px;transform:scale(.8);transform-origin:0 0;background:var(--white);overflow:hidden}
.abs{position:absolute}
.caps{text-transform:uppercase;letter-spacing:.08em}
.center{text-align:center}

.topbar{left:0;top:0;width:569px;height:14px;background:var(--yellow);color:var(--white);font-size:3.5px;font-weight:600}
.topbar .shipping-note{position:absolute;left:12px;top:5px}
.topbar .account{position:absolute;right:12px;top:5px;display:flex;gap:8px}

.header{left:0;top:14px;width:569px;height:58px;background:var(--white)}
.nav{position:absolute;top:26px;display:flex;gap:10px;font-size:4.5px;font-weight:600}
.search{position:absolute;left:12px;top:24px;display:flex;align-items:center;gap:4px;font-size:4.5px;font-weight:600}
.brand{position:absolute;left:234px;top:8px;width:100px;text-align:center}
.brand .mark{display:block;width:18px;height:18px;border-radius:50%;background:var(--yellow);margin:0 auto 6px}
.brand .name{font-size:13px;font-weight:500;letter-spacing:-.02em}
.cart{position:absolute;right:12px;top:23px;display:flex;align-items:center;gap:4px;font-size:4.5px;font-weight:600}
.cart .count{width:8px;height:8px;border-radius:50%;background:var(--yellow);color:var(--white);font-size:4px;display:flex;align-items:center;justify-content:center}

.hero{left:0;top:72px;width:569px;height:285px;background:radial-gradient(ellipse at 50% 35%,#6b4a2a 0%,#4a3a22 22%,#5f7a3c 45%,#7fa05a 75%,#9bb878 100%)}
.hero-title{left:0;top:190px;width:569px;color:var(--white);font-size:17px;font-weight:500;letter-spacing:.06em}
.hero-sub{left:0;top:214px;width:569px;color:var(--white);font-size:8.5px}
.btn{display:flex;align-items:center;justify-content:center;font-size:4.5px;font-weight:700;letter-spacing:.1em;text-transform:uppercase}
.btn-yellow{background:var(--yellow);color:var(--white)}
.btn-grey{background:var(--grey-btn);color:var(--white)}
.btn-white{background:var(--white);color:var(--ink)}

.section-title{left:0;width:569px;font-size:17px;font-weight:300;letter-spacing:.03em}
.section-sub{left:0;width:569px;font-size:6px;line-height:11px;color:#444}
.pets-photo{left:199px;top:435px;width:173px;height:120px;background:radial-gradient(ellipse at 30% 75%,#8a6e4e 0%,#8a6e4e 20%,transparent 45%),radial-gradient(ellipse at 65% 50%,#e8d3a8 0%,#e2c795 30%,transparent 60%),var(--white)}

.card{width:96px;height:117px;border:1px solid var(--line);background:var(--white)}
.card.active{border-color:var(--yellow)}
.card .pack{position:absolute;left:30px;top:20px;width:36px;height:72px;border-radius:2px}
.card .tag{position:absolute;left:24px;top:84px;background:#e43c3c;color:var(--white);font-size:4.5px;padding:1px 2px;font-weight:600}
.card-name{width:96px;font-size:4.2px;line-height:7px;font-weight:600}
.card-price{width:96px;font-size:5.5px;color:var(--price)}

.offer-band{left:0;top:872px;width:569px;height:213px;background:var(--yellow)}
.offer-box{left:137px;top:905px;width:109px;height:155px;background:linear-gradient(160deg,#ffffff 0%,#f1f1f1 40%,#7fbf58 75%,#3e9b3a 100%);border-radius:2px}
.offer-title{left:290px;top:929px;color:var(--white);font-size:10px;font-weight:600;letter-spacing:.14em}
.offer-start{left:290px;top:944px;color:var(--white);font-size:5.5px;font-weight:600;letter-spacing:.12em}
.offer-copy{left:290px;top:961px;width:185px;color:var(--white);font-size:5.3px;line-height:10.5px}

.post-img{top:1121px;width:154px;height:71px}
.post-title{top:1201px;font-size:6.8px;font-weight:600;letter-spacing:.1em}
.post-copy{top:1212px;width:130px;font-size:4.8px;line-height:7px;color:#666}
.post-more{top:1238px;font-size:3.8px;font-weight:600;color:var(--yellow);letter-spacing:.1em}

.footer{left:0;top:1278px;width:569px;height:200px;background:var(--footer)}
.newsletter-title{left:0;top:1306px;width:569px;font-size:4.8px;font-weight:600}
.newsletter-input{left:219px;top:1319px;width:98px;height:14px;background:var(--white);font-size:3.6px;color:#999;padding:5px 6px}
.newsletter-submit{left:317px;top:1319px;width:33px;height:14px}
.col{top:1360px}
.col h4{font-size:4.8px;font-weight:600;margin-bottom:5px;letter-spacing:.08em;text-transform:uppercase}
.col li{list-style:none;font-size:3.6px;line-height:10.5px;color:#666;letter-spacing:.08em;text-transform:uppercase}
.col li.current{color:var(--yellow)}

.bottombar{left:0;top:1478px;width:569px;height:22px;background:var(--yellow)}
.copyright{position:absolute;left:76px;top:9px;font-size:3.8px;color:var(--white)}
.social{position:absolute;left:437px;top:8px;display:flex;gap:11px}
.social span{width:5px;height:5px;border-radius:50%;background:var(--white)}
</style>
</head>
<body>
<div class="page">

  <div class="abs topbar caps">
    <span class="shipping-note">Free shipping when you spend £50 or more</span>
    <span class="account"><span>My account</span><span>Login</span><span>0800 123 4567</span></span>
  </div>

  <header class="abs header">
    <div class="search caps">
      <svg width="7" height="7" viewBox="0 0 10 10"><circle cx="4" cy="4" r="3" fill="none" stroke="#2b2b2b" stroke-width="1.2"/><line x1="6.3" y1="6.3" x2="9" y2="9" stroke="#2b2b2b" stroke-width="1.2"/></svg>
      Search
    </div>
    <nav class="nav caps" style="left:155px"><span>Home</span><span>Dogs</span><span>Cats</span></nav>
    <div class="brand"><span class="mark"></span><span class="name">Brixtondel</span></div>
    <nav class="nav caps" style="left:350px"><span>Shop</span><span>Blog</span><span>Contact us</span></nav>
    <div class="cart caps">
      <svg width="7" height="7" viewBox="0 0 10 10"><path d="M1.5 3h7l-.6 6h-5.8z M3.5 3V2a1.5 1.5 0 0 1 3 0v1" fill="none" stroke="#2b2b2b" stroke-width="1"/></svg>
      Cart <span class="count">0</span>
    </div>
  </header>

  <section>
    <div class="abs hero" role="img" aria-label="Photograph of a German Shepherd dog in a green field"></div>
    <h1 class="abs hero-title center caps">Our pets deserves the best</h1>
    <p class="abs hero-sub center">Treat them to the good stuffs</p>
    <a class="abs btn btn-yellow" style="left:245px;top:241px;width:78px;height:16px">Shop now</a>
  </section>

  <section>
    <h2 class="abs section-title center" style="top:388px">Our Products</h2>
    <p class="abs section-sub center" style="top:412px">Treat them to the good stuffs</p>
    <div class="abs pets-photo" role="img" aria-label="Photograph of a tabby cat lying beside a Labrador puppy"></div>
    <a class="abs btn btn-grey" style="left:219px;top:572px;width:60px;height:16px">For cats</a>
    <a class="abs btn btn-yellow" style="left:290px;top:572px;width:60px;height:16px">For dogs</a>
  </section>

  <section>
    <h2 class="abs section-title center" style="top:619px">Our Best Sellers</h2>
    <p class="abs section-sub center" style="top:643px">Lorem ipsum, or lipsum as it is sometimes known, is dummy text used in<br>laying out print, graphic or web designs.</p>

    <div class="abs card active" style="left:76px;top:684px">
      <div class="pack" style="background:linear-gradient(#7d8a3e,#b49a5c 55%,#d9c69a)" role="img" aria-label="Bag of adult dog food"></div>
      <span class="tag">Save 15%</span>
    </div>
    <div class="abs card" style="left:183px;top:684px">
      <div class="pack" style="background:linear-gradient(#e9e9e9,#9a9a9a 55%,#d6d6d6)" role="img" aria-label="Bag of cat food"></div>
    </div>
    <div class="abs card" style="left:290px;top:684px">
      <div class="pack" style="background:linear-gradient(#2b3c8f,#3b5bb0 50%,#4b78c9)" role="img" aria-label="Bag of cat food"></div>
    </div>
    <div class="abs card" style="left:396px;top:684px">
      <div class="pack" style="left:32px;width:32px;background:linear-gradient(#f39a1c,#f7c64a 50%,#3c7fc1)" role="img" aria-label="Pack of dental dog treats"></div>
    </div>

    <p class="abs card-name center caps" style="left:76px;top:813px">Harwood Meadow turkey<br>&amp; rice adult dog food 15kg</p>
    <p class="abs card-name center caps" style="left:183px;top:813px">Harwood Meadow turkey<br>&amp; rice adult dog food 15kg</p>
    <p class="abs card-name center caps" style="left:290px;top:813px">Harwood Meadow turkey<br>&amp; rice adult dog food 15kg</p>
    <p class="abs card-name center caps" style="left:396px;top:813px">Harwood Meadow turkey<br>&amp; rice adult dog food 15kg</p>
    <p class="abs card-price center" style="left:76px;top:830px">£104.89</p>
    <p class="abs card-price center" style="left:183px;top:830px">£104.89</p>
    <p class="abs card-price center" style="left:290px;top:830px">£104.89</p>
    <p class="abs card-price center" style="left:396px;top:830px">£104.89</p>
  </section>

  <section>
    <div class="abs offer-band"></div>
    <div class="abs offer-box" role="img" aria-label="Box of joint supplement for dogs"></div>
    <h3 class="abs offer-title caps">Save up to 40%</h3>
    <p class="abs offer-start caps">Starting at: $3.79</p>
    <p class="abs offer-copy">Lorem ipsum, or lipsum as it is sometimes known, is dummy text used in laying out print, graphic or web designs. The passage is attributed to an unknown typesetter in the 15th century who is thought to have scrambled parts of Cicero's De Finibus Bonorum et Malorum for use in a type specimen book.</p>
    <a class="abs btn btn-white" style="left:290px;top:1026px;width:64px;height:16px">Shop now</a>
  </section>

  <section>
    <div class="abs post-img" style="left:18px;background:linear-gradient(90deg,#4f7a33,#7a5a3a 55%,#8db069)" role="img" aria-label="Photograph of a German Shepherd in profile"></div>
    <div class="abs post-img" style="left:208px;background:linear-gradient(90deg,#f0b2bf,#e8dcd4 50%,#f2a9b8)" role="img" aria-label="Photograph of dogs and cats on a pink background"></div>
    <div class="abs post-img" style="left:398px;background:linear-gradient(90deg,#2a1f18,#7a6a5c 55%,#3a2c22)" role="img" aria-label="Photograph of a tabby cat in profile"></div>

    <h3 class="abs post-title caps" style="left:18px">Our dog can now work</h3>
    <h3 class="abs post-title caps" style="left:208px">Our pets are now healthy</h3>
    <h3 class="abs post-title caps" style="left:398px">Some cats are not active</h3>
    <p class="abs post-copy" style="left:18px">Brixtondel is a premier supplier of Pet Supplies to the UK market</p>
    <p class="abs post-copy" style="left:208px">Brixtondel is a premier supplier of Pet Supplies to the UK market</p>
    <p class="abs post-copy" style="left:398px">Brixtondel is a premier supplier of Pet Supplies to the UK market</p>
    <a class="abs post-more caps" style="left:18px">Read more</a>
    <a class="abs post-more caps" style="left:208px">Read more</a>
    <a class="abs post-more caps" style="left:398px">Read more</a>
  </section>

  <footer>
    <div class="abs footer"></div>
    <p class="abs newsletter-title center caps">Subscribe to our newsletter</p>
    <div class="abs newsletter-input caps">Enter your email address</div>
    <a class="abs btn btn-yellow newsletter-submit" style="font-size:3.6px">Submit</a>

    <div class="abs col" style="left:101px">
      <h4>About us</h4>
      <ul><li class="current">Our company</li><li>FAQ</li><li>Contact us</li><li>Privacy policy</li><li>Shipping fee</li></ul>
    </div>
    <div class="abs col" style="left:207px">
      <h4>For dogs</h4>
      <ul><li>Orthopaedic dog beds</li><li>Vet bed</li><li>Cool coats</li><li>Slow feed dog bowls</li><li>Automatic dog feeder</li><li>Drinking fountain</li><li>Collapsible drinking bowls</li></ul>
    </div>
    <div class="abs col" style="left:314px">
      <h4>For cats</h4>
      <ul><li>Beautiful cat</li><li>Vet bed</li><li>Cat nip toys</li><li>Scratch posts</li><li>Automatic cat</li><li>Drinking fountain</li></ul>
    </div>
    <div class="abs col" style="left:421px">
      <h4>News &amp; articles</h4>
      <ul><li>Our dog can now work</li><li>Our pets are now healthy</li><li>Some cats are not active</li></ul>
    </div>

    <div class="abs bottombar">
      <span class="copyright">© Copyright 2016 Brixtondel Limited</span>
      <span class="social"><span></span><span></span><span></span><span></span></span>
    </div>
  </footer>

</div>
</body>
</html>
```